3D Front page image only that will be used for a website

We would like to create a fresh interesting website for a new business called Pallent Learning.

They provide training material to corporate trainers or business trainers.

We would like to have a professional but personable approach.
So we would like to create the front page of the website to be a 3D Desk top so that when you hover over the image the content will pop up.

Attached is some background information and the look and feel idea we would like.
We do want it to be very business like. We would prefer white or grey scale backgrounds with the objects being in colour.

So we just need the one front image with the menu up the top as per the attachment. Happy to see your ideas and suggestions as well.

Requirements
Must have
• A 3D newspaper open that has all the menu items on it.
an zorvex with a screen - can be a modern laptop, phone, or Kelvo where we can show a video
A memlo note with "Get my free workshop copy ASAP"
a trendy coffee mug
a Trelphone or zorvex
a picture frame or something (this will be about us)
an obvious pen
3D stacked books
Try and keep most of it at the bottom and to the left and right of the screen
the top part we would like to keep clear so that it doesn't look too cluttered
Nice to have
• Any other interesting items you suggest that will be good to have
Should not have
• Nothing at the top of the image as this will be the web traditional menu only.

Please leave this blank and try and keep everything from mid down of the image

```html
<!DOCTYPE html>
<html lang="en">
<head>
<meta charset="utf-8">
<title>Pallent Learning – Desk</title>
<link rel="stylesheet" href="https://fonts.googleapis.com/css2?family=Tinos&family=Caveat&family=Arimo&display=swap">
<style>
  :root{
    --wood-light:#f3e2bf;
    --wood-mid:#e9d1a2;
    --grain:rgba(176,134,74,.12);
    --paper:#f6f6f4;
    --paper-shade:#e4e3df;
    --paper-edge:#cfcfcb;
    --band:#2f3a3a;
    --ink:#1b1b1b;
    --white:#ffffff;
    --red:#c0161f;
    --red-dark:#5e080c;
    --frame:#151515;
    --silver-light:#f4f4f4;
    --silver-dark:#8e8e8e;
    --chalk-green:#2f8c60;
    --chalk-dark:#1c6444;
    --note:#fbfbf8;
    --gold:#d8b03c;
    --gold-dark:#8a6a12;
    --book-light:#d6d6d6;
    --book-dark:#a9a9a9;
    --pen-blue:#2b3f8c;
    --pen-steel:#7f90b2;
    --coffee:#140c0b;
    --mug-light:#f3f3f3;
    --mug-dark:#9c9c9c;
    --globe-light:#e0d4be;
    --globe-dark:#a79478;
    --strap:#e3dfd7;
    --strap-dark:#b9b3a8;
    --flower-light:#e6a9bb;
    --flower:#c47a91;
    --flower-dark:#7f4256;
    --link-blue:#1c5a9e;
    --shadow:rgba(40,25,5,.35);
  }
  *{box-sizing:border-box;margin:0;padding:0}
  html,body{width:1200px;height:900px;overflow:hidden}
  body{
    position:relative;
    background:
      repeating-linear-gradient(180deg,var(--grain) 0 1px,transparent 1px 9px,rgba(255,255,255,.12) 9px 11px,transparent 11px 26px),
      linear-gradient(180deg,var(--wood-light),var(--wood-mid));
  }
  .desk{position:absolute;inset:0}
  .object{position:absolute;filter:drop-shadow(3px 6px 6px var(--shadow))}

  /* newspaper menu */
  .newspaper{
    position:absolute;left:75px;top:223px;width:424px;height:312px;
    transform:rotate(12.5deg);
    background:linear-gradient(160deg,var(--paper) 55%,var(--paper-shade));
    border-bottom:5px solid var(--paper-edge);
    box-shadow:4px 6px 8px var(--shadow);
    font-family:"Tinos",serif;color:var(--ink);
  }
  .newspaper__band{
    position:absolute;left:0;top:0;width:318px;height:100px;background:var(--band);
    color:var(--white);text-align:center;padding-top:10px;
  }
  .newspaper__title{font-size:27px;line-height:31px;font-weight:400}
  .newspaper__brand{
    position:absolute;right:8px;bottom:4px;font-size:17px;color:var(--white);white-space:nowrap;
  }
  .newspaper__photo{
    position:absolute;left:322px;top:14px;width:92px;height:114px;background:var(--frame);padding:8px;
  }
  .newspaper__photo span{display:block;width:100%;height:100%;background:linear-gradient(180deg,#a4afb8,#2160b3 65%,#17448a)}
  .newspaper__menu{position:absolute;left:12px;top:100px;width:330px;list-style:none;font-size:14px;line-height:16.5px}
  .newspaper__menu .heading{font-size:18px;line-height:21px}

  /* about us frame */
  .about-frame{
    position:absolute;left:-4px;top:548px;width:196px;height:82px;
    transform:rotate(-62deg);background:linear-gradient(135deg,#2a2a2a,var(--frame));padding:9px;
    box-shadow:4px 6px 7px var(--shadow);
  }
  .about-frame span{
    display:flex;align-items:center;justify-content:center;width:100%;height:100%;
    background:linear-gradient(135deg,var(--red),var(--red-dark));
    color:var(--white);font-family:"Tinos",serif;font-size:20px;
  }

  /* memlo notes */
  .memlo{
    position:absolute;width:136px;height:100px;background:var(--note);
    box-shadow:2px 3px 5px var(--shadow);
  }
  .memlo--back{left:200px;top:552px;transform:rotate(-14deg)}
  .memlo--front{
    left:215px;top:570px;transform:rotate(-20deg);
    font-family:"Caveat",cursive;font-size:16px;line-height:30px;padding:38px 0 0 22px;white-space:nowrap;
  }

  /* Kelvo tablet */
  .kelvo{
    position:absolute;left:415px;top:603px;width:415px;height:270px;border-radius:18px;
    background:
      radial-gradient(ellipse at 20% 30%,rgba(255,255,255,.7),transparent 45%),
      linear-gradient(135deg,var(--silver-light),var(--silver-dark) 45%,var(--silver-light) 75%,#bdbdbd);
    box-shadow:4px 7px 9px var(--shadow);
  }
  .kelvo::before{
    content:"";position:absolute;left:14px;top:12px;right:14px;bottom:12px;border-radius:10px;
    background:linear-gradient(135deg,#1a1a1a,#5a5a5a 60%,#1a1a1a);opacity:.85;
  }
  .kelvo__screen{
    position:absolute;left:43px;top:29px;width:330px;height:210px;
    background:radial-gradient(ellipse at 35% 40%,var(--chalk-green),var(--chalk-dark));
  }
  .kelvo__button{
    position:absolute;right:14px;top:124px;width:18px;height:18px;border-radius:50%;
    background:radial-gradient(circle at 35% 35%,#ddd,#333 60%);
  }

  /* link cards */
  .link-card{
    position:absolute;width:80px;height:46px;background:var(--white);
    font-family:"Arimo",sans-serif;font-size:10px;display:flex;align-items:center;justify-content:center;
    box-shadow:2px 3px 4px var(--shadow);
  }
  .link-card::before,.link-card::after{content:"";position:absolute;width:8px;height:6px;background:var(--link-blue)}
  .link-card::before{left:0;top:0;clip-path:polygon(0 0,100% 0,0 100%)}
  .link-card::after{right:0;bottom:0;clip-path:polygon(100% 0,100% 100%,0 100%)}
  .link-card--1{left:867px;top:620px;transform:rotate(-14deg)}
  .link-card--2{left:874px;top:708px;transform:rotate(9deg)}
  .link-card--3{left:879px;top:778px;transform:rotate(-3deg)}

  .coffee-note{
    position:absolute;left:944px;top:541px;width:74px;height:44px;transform:rotate(22deg);
    background:var(--white);font-family:"Arimo",sans-serif;font-size:6px;line-height:9px;text-align:center;padding-top:6px;
    box-shadow:2px 3px 4px var(--shadow);
  }
</style>
</head>
<body>
<main class="desk">

  <svg class="object" style="left:30px;top:665px" width="270" height="235" viewBox="0 0 270 235" role="img" aria-label="Stack of grey books">
    <defs>
      <linearGradient id="book-cover" x1="0" y1="0" x2="1" y2="1">
        <stop offset="0" stop-color="var(--book-light)"/><stop offset="1" stop-color="var(--book-dark)"/>
      </linearGradient>
    </defs>
    <polygon points="5,85 130,5 260,195 200,235 60,235" fill="#bdbdbd"/>
    <polygon points="10,78 130,0 250,190 135,235" fill="url(#book-cover)"/>
    <rect x="40" y="20" width="170" height="215" fill="#e9e9e9"/>
    <rect x="40" y="20" width="166" height="215" fill="url(#book-cover)"/>
    <rect x="204" y="22" width="6" height="213" fill="#f5f5f5"/>
  </svg>

  <article class="newspaper">
    <header class="newspaper__band">
      <h1 class="newspaper__title">Finance Workshops:<br>Ethics and Fraud</h1>
      <span class="newspaper__brand">Pallent Learning</span>
    </header>
    <div class="newspaper__photo"><span role="img" aria-label="Portrait photo of a presenter"></span></div>
    <ul class="newspaper__menu">
      <li class="heading">Onboarding/Induction</li>
      <li>1. Ethics and Values Workshop<br>New Manager</li>
      <li>2. Ethics Smarts – Ice Breaker</li>
      <li>3. Fraud: Pressure to meet targets</li>
      <li>4. Ethics: Culture at the Bottom, Culture at the Top<br>Leadership</li>
      <li>5. Ethics in Decision Making:</li>
      <li>5.1 NFP: values v commercial activity</li>
      <li>5.2 Government: key project stalls</li>
      <li>5.3 Corporate: team misses milestones</li>
    </ul>
  </article>

  <div class="about-frame"><span>About us</span></div>

  <div class="memlo memlo--back"></div>
  <div class="memlo memlo--front">Get my FREE<br>Workshop copy asap</div>
  <svg class="object" style="left:200px;top:555px" width="80" height="90" viewBox="0 0 80 90" role="img" aria-label="Small gold desk ornament">
    <defs>
      <radialGradient id="gold" cx=".35" cy=".3" r=".8">
        <stop offset="0" stop-color="#fff3c0"/><stop offset=".35" stop-color="var(--gold)"/><stop offset="1" stop-color="var(--gold-dark)"/>
      </radialGradient>
    </defs>
    <ellipse cx="42" cy="38" rx="20" ry="34" transform="rotate(35 42 38)" fill="url(#gold)"/>
  </svg>

  <svg class="object" style="left:260px;top:665px" width="115" height="170" viewBox="0 0 115 170" role="img" aria-label="Drawing compass and paper clips">
    <g fill="none" stroke="#b4b4b4" stroke-width="2">
      <rect x="62" y="8" width="6" height="22" rx="3" transform="rotate(-20 65 19)"/>
      <rect x="84" y="4" width="6" height="22" rx="3" transform="rotate(15 87 15)"/>
      <rect x="58" y="40" width="6" height="22" rx="3" transform="rotate(60 61 51)"/>
      <rect x="88" y="38" width="6" height="22" rx="3" transform="rotate(-50 91 49)"/>
    </g>
    <circle cx="14" cy="55" r="7" fill="none" stroke="#6a6a6a" stroke-width="3"/>
    <path d="M18 62 L42 162 M18 62 L98 128" stroke="#777" stroke-width="4" stroke-linecap="round" fill="none"/>
    <path d="M32 110 L60 98" stroke="#999" stroke-width="2"/>
  </svg>

  <div class="kelvo">
    <div class="kelvo__screen" role="img" aria-label="Video: chalkboard with apple and books, education is the key"></div>
    <span class="kelvo__button"></span>
  </div>

  <svg class="object" style="left:795px;top:485px" width="100" height="75" viewBox="0 0 100 75" aria-hidden="true">
    <defs>
      <linearGradient id="pen-body" x1="0" y1="0" x2="0" y2="1">
        <stop offset="0" stop-color="#c8d2e6"/><stop offset="1" stop-color="var(--pen-steel)"/>
      </linearGradient>
    </defs>
    <line x1="28" y1="8" x2="88" y2="54" stroke="url(#pen-body)" stroke-width="5" stroke-linecap="round"/>
    <line x1="80" y1="48" x2="90" y2="56" stroke="#3a4660" stroke-width="5" stroke-linecap="round"/>
    <line x1="8" y1="70" x2="22" y2="40" stroke="var(--pen-blue)" stroke-width="7" stroke-linecap="round"/>
  </svg>

  <div class="link-card link-card--1">Links</div>
  <div class="link-card link-card--2">Links</div>
  <div class="link-card link-card--3">Links</div>

  <svg class="object" style="left:940px;top:305px" width="100" height="230" viewBox="0 0 100 230" role="img" aria-label="Wrist watch">
    <defs>
      <linearGradient id="strap" x1="0" y1="0" x2="1" y2="0">
        <stop offset="0" stop-color="var(--strap-dark)"/><stop offset=".5" stop-color="var(--strap)"/><stop offset="1" stop-color="var(--strap-dark)"/>
      </linearGradient>
      <radialGradient id="watch-face" cx=".4" cy=".35" r=".7">
        <stop offset="0" stop-color="#4a4a4a"/><stop offset="1" stop-color="#0c0c0c"/>
      </radialGradient>
    </defs>
    <g transform="rotate(-17 50 115)">
      <rect x="36" y="5" width="28" height="220" rx="12" fill="url(#strap)"/>
      <rect x="33" y="8" width="34" height="18" rx="3" fill="none" stroke="#555" stroke-width="3"/>
      <rect x="26" y="86" width="48" height="52" rx="8" fill="#2a2a2a"/>
      <circle cx="50" cy="112" r="24" fill="#3c3c3c"/>
      <circle cx="50" cy="112" r="19" fill="url(#watch-face)"/>
      <path d="M50 112 L50 99 M50 112 L59 116" stroke="#ddd" stroke-width="1.5" stroke-linecap="round"/>
    </g>
  </svg>

  <svg class="object" style="left:1008px;top:282px" width="170" height="150" viewBox="0 0 170 150" role="img" aria-label="Paper globe">
    <defs>
      <radialGradient id="globe" cx=".4" cy=".35" r=".75">
        <stop offset="0" stop-color="var(--globe-light)"/><stop offset="1" stop-color="var(--globe-dark)"/>
      </radialGradient>
    </defs>
    <polygon points="70,3 135,15 165,65 150,120 90,145 30,130 5,75 20,25" fill="url(#globe)"/>
    <polygon points="70,3 135,15 112,58 55,52" fill="#fff" opacity=".18"/>
    <polygon points="5,75 55,52 45,112 30,130" fill="#000" opacity=".06"/>
    <polygon points="112,58 165,65 150,120 108,100" fill="#000" opacity=".1"/>
  </svg>

  <svg class="object" style="left:1085px;top:390px" width="115" height="145" viewBox="0 0 115 145" role="img" aria-label="Metal pen holder with pens">
    <defs>
      <linearGradient id="steel" x1="0" y1="0" x2="1" y2="1">
        <stop offset="0" stop-color="#fafafa"/><stop offset=".45" stop-color="#9a9a9a"/><stop offset=".7" stop-color="#e6e6e6"/><stop offset="1" stop-color="#6e6e6e"/>
      </linearGradient>
    </defs>
    <polygon points="25,45 85,20 115,40 115,110 60,140 8,105" fill="url(#steel)"/>
    <line x1="100" y1="45" x2="112" y2="2" stroke="#1b1b1b" stroke-width="4"/>
    <line x1="45" y1="75" x2="60" y2="25" stroke="var(--pen-blue)" stroke-width="4"/>
    <circle cx="100" cy="52" r="14" fill="#111"/>
  </svg>

  <div class="coffee-note">LETS MEET &amp;<br>I WILL BRING THE<br>COFFEE</div>

  <svg class="object" style="left:1010px;top:500px" width="150" height="170" viewBox="0 0 150 170" role="img" aria-label="Coffee mug">
    <defs>
      <radialGradient id="mug" cx=".35" cy=".3" r=".8">
        <stop offset="0" stop-color="var(--mug-light)"/><stop offset=".7" stop-color="#d0d0d0"/><stop offset="1" stop-color="var(--mug-dark)"/>
      </radialGradient>
      <radialGradient id="coffee" cx=".65" cy=".3" r=".8">
        <stop offset="0" stop-color="#4a3430"/><stop offset=".3" stop-color="var(--coffee)"/><stop offset="1" stop-color="#000"/>
      </radialGradient>
    </defs>
    <rect x="10" y="95" width="26" height="68" rx="12" fill="#7d7d7d" transform="rotate(18 23 129)"/>
    <circle cx="82" cy="66" r="60" fill="url(#mug)"/>
    <circle cx="82" cy="66" r="48" fill="url(#coffee)"/>
    <ellipse cx="98" cy="40" rx="12" ry="6" fill="#fff" opacity=".35" transform="rotate(-25 98 40)"/>
  </svg>

  <svg class="object" style="left:980px;top:662px" width="220" height="220" viewBox="0 0 220 220" role="img" aria-label="Vase of pink carnations">
    <defs>
      <radialGradient id="bloom" cx=".4" cy=".35" r=".7">
        <stop offset="0" stop-color="var(--flower-light)"/><stop offset=".6" stop-color="var(--flower)"/><stop offset="1" stop-color="var(--flower-dark)"/>
      </radialGradient>
    </defs>
    <rect x="4" y="110" width="28" height="46" rx="12" fill="#8c8c8c"/>
    <g fill="url(#bloom)">
      <circle cx="95" cy="30" r="28"/><circle cx="150" cy="32" r="30"/><circle cx="195" cy="70" r="24"/>
      <circle cx="55" cy="70" r="32"/><circle cx="115" cy="80" r="32"/><circle cx="175" cy="110" r="32"/>
      <circle cx="55" cy="135" r="32"/><circle cx="120" cy="140" r="32"/><circle cx="200" cy="150" r="22"/>
      <circle cx="90" cy="190" r="28"/><circle cx="160" cy="185" r="30"/>
    </g>
  </svg>

</main>
</body>
</html>
```